Original business card of a small accounting firm

My firm specializes in accounting and taxes for small businesses. I'm looking for an original and creative business card as a marketing tool to give to prospective clients; however since we are a professional firm the card must also appear professional. I'm uploading a few examples of what I believe may fit my needs. Please feel free to use them as a jumping off point. Lastly, I'm uploading the company logo which I'd like to be the focal point on the back of the card and somewhat incorporated on the front on a smaller scale. I hope my description was helpful.
Target Market(s)
Tax clients and small businesses
Industry/Entity Type
Accounting
Contact Information for Business Card
Gerald Whitcombe
Certified Public Accountant │President
Whitcombe Advisors
T│ (555) 417-2863
Email│GWhitcombe@WhitcombeAdvisors.example
Look and feel
Each slider illustrates characteristics of the customer's brand and the style your logo design should communicate.

```html
<!DOCTYPE html>
<html lang="en">
<head>
<meta charset="utf-8">
<title>Whitcombe Advisors – Business Card</title>
<link rel="stylesheet" href="https://fonts.googleapis.com/css2?family=Open+Sans:wght@400;600;700&display=swap">
<style>
  :root {
    --page-bg: #e4e4e4;
    --card-bg: #ffffff;
    --ink: #2f2f2f;
    --ink-soft: #444444;
    --brand-blue: #2f5db3;
    --brand-steel: #4a5fa8;
    --divider: #dedede;
    --shadow: rgba(0, 0, 0, 0.22);
  }
  * { box-sizing: border-box; margin: 0; padding: 0; }
  html, body {
    width: 1200px;
    height: 852px;
    overflow: hidden;
    background: var(--page-bg);
    font-family: "Open Sans", Arial, sans-serif;
    color: var(--ink);
  }
  .stage { position: relative; width: 1200px; height: 852px; }

  .card {
    position: absolute;
    width: 520px;
    height: 300px;
    background: var(--card-bg);
    border-radius: 22px;
    box-shadow: 0 6px 16px var(--shadow);
    overflow: hidden;
  }
  .card--back { left: 90px; top: 100px; }
  .card--front { left: 590px; top: 452px; }

  .wordmark {
    display: flex;
    align-items: center;
    gap: 10px;
    font-weight: 700;
    color: var(--brand-steel);
    white-space: nowrap;
  }
  .wordmark__square { background: var(--brand-steel); flex: none; }

  .card--back .wordmark {
    position: absolute;
    left: 50%; top: 50%;
    transform: translate(-50%, -50%);
    font-size: 34px;
  }
  .card--back .wordmark__square { width: 30px; height: 30px; }

  .card--front .wordmark {
    position: absolute;
    left: 22px; top: 150px;
    transform: translateY(-50%);
    font-size: 17px;
    gap: 7px;
  }
  .card--front .wordmark__square { width: 16px; height: 16px; }

  .card__divider {
    position: absolute;
    left: 236px; top: 0; bottom: 0;
    width: 1px;
    background: var(--divider);
  }

  .details {
    position: absolute;
    left: 254px; top: 34px; right: 14px;
  }
  .details__name {
    font-size: 19px;
    font-weight: 700;
    color: var(--brand-blue);
    line-height: 1.2;
  }
  .details__title {
    margin-top: 4px;
    font-size: 11.5px;
    line-height: 1.45;
    color: var(--ink-soft);
  }
  .contact {
    list-style: none;
    margin-top: 74px;
    font-size: 11px;
    line-height: 1.2;
  }
  .contact__item {
    display: flex;
    align-items: center;
    gap: 8px;
    margin-bottom: 8px;
    white-space: nowrap;
  }
  .contact__icon { width: 12px; height: 12px; flex: none; fill: var(--brand-steel); }
</style>
</head>
<body>
<main class="stage">
  <section class="card card--back" aria-label="Card back">
    <div class="wordmark">
      <span class="wordmark__square"></span>
      <span class="wordmark__name">Whitcombe Advisors</span>
    </div>
  </section>

  <section class="card card--front" aria-label="Card front">
    <div class="wordmark">
      <span class="wordmark__square"></span>
      <span class="wordmark__name">Whitcombe Advisors</span>
    </div>

    <div class="card__divider"></div>

    <div class="details">
      <h1 class="details__name">Gerald Whitcombe</h1>
      <p class="details__title">Certified Public Accountant/<br>President Whitcombe Advisors</p>

      <ul class="contact">
        <li class="contact__item">
          <svg class="contact__icon" viewBox="0 0 16 16" aria-hidden="true"><path d="M3.5 1.5l2.5 2.6-1.4 1.8c.9 2 2.5 3.6 4.5 4.5l1.8-1.4 2.6 2.5-1.6 2.5C6.6 13.6 2.4 9.4 1 3.1z"/></svg>
          <span>(555) 417-2863</span>
        </li>
        <li class="contact__item">
          <svg class="contact__icon" viewBox="0 0 16 16" aria-hidden="true"><path d="M1 3h14v10H1z M2.2 4.2L8 8.6l5.8-4.4z" fill-rule="evenodd"/></svg>
          <span>GWhitcombe@WhitcombeAdvisors.example</span>
        </li>
        <li class="contact__item">
          <svg class="contact__icon" viewBox="0 0 16 16" aria-hidden="true"><circle cx="8" cy="8" r="7"/><path d="M1 8h14M8 1c-3 3.5-3 10.5 0 14M8 1c3 3.5 3 10.5 0 14" stroke="#fff" stroke-width="1" fill="none"/></svg>
          <span>www.WhitcombeAdvisors.example</span>
        </li>
      </ul>
    </div>
  </section>
</main>
</body>
</html>
```